We need a flyer design for a new fencing business. We do ferrowane fencing instalations and pride our company on Reliabilty, Dependabilty and genuine quality. Because it's not just a fence... It's your fence. Our company offers customer free quotes. Things that would need to be on the flyer;

*Company Name - Valley Copperpath Fencing
*Company email - copperpathfencing@quillmail.net
*Company Phone number - 0455 912 307

*Ferrowane fence specialist
*Free quotes

```html
<!DOCTYPE html>
<html lang="en">
<head>
<meta charset="utf-8">
<title>Valley Copperpath Fencing Flyer</title>
<link rel="stylesheet" href="https://fonts.googleapis.com/css2?family=Almendra&family=Arimo:ital,wght@0,400;0,700;1,700&display=swap">
<style>
  :root {
    --page: #ffffff;
    --fence-dark: #2f6b3a;
    --fence-mid: #5a9163;
    --fence-light: #7fb184;
    --lattice-light: #f6f1de;
    --lattice-mid: #e4dcbc;
    --band-green: #5b8b58;
    --accent-green: #6b9a68;
    --ink: #111111;
    --white: #ffffff;
  }
  * { margin: 0; padding: 0; box-sizing: border-box; }
  html, body { width: 1200px; height: 800px; overflow: hidden; background: var(--page); }
  .flyer { position: relative; width: 1200px; height: 800px; background: var(--page); font-family: "Arimo", Arial, sans-serif; color: var(--ink); }

  .fence-visual {
    position: absolute; left: 25px; top: 25px; width: 1150px; height: 303px;
    background: linear-gradient(180deg, var(--fence-mid) 0%, var(--fence-light) 45%, var(--fence-mid) 100%);
  }
  .fence-visual::after {
    content: ""; position: absolute; inset: 0;
    background: linear-gradient(180deg, var(--lattice-mid) 0, var(--lattice-light) 55px, var(--fence-dark) 62px, transparent 75px);
    opacity: .9;
  }
  .lattice-band {
    position: absolute; left: 25px; width: 1150px;
    background: radial-gradient(ellipse at center, var(--white) 0%, var(--lattice-light) 60%, var(--lattice-mid) 100%);
  }
  .lattice-band--upper { top: 328px; height: 170px; }
  .lattice-band--lower { top: 658px; height: 117px; }
  .rule { position: absolute; left: 25px; width: 1150px; background: var(--band-green); }
  .rule--upper { top: 497px; height: 18px; }
  .rule--lower { top: 640px; height: 18px; }

  .brand-name {
    position: absolute; left: 0; width: 1300px; top: 140px; text-align: center;
    font-family: "Almendra", Georgia, serif; font-size: 66px; font-weight: 400;
    color: var(--white); letter-spacing: 1px;
    text-shadow: 0 0 10px rgba(0,0,0,.85), 0 0 22px rgba(0,0,0,.6);
  }
  .service-line {
    position: absolute; left: 385px; top: 236px;
    font-size: 20px; font-weight: 700; font-style: italic; letter-spacing: .3px;
    text-shadow: 0 0 8px var(--white), 0 0 16px var(--white), 0 0 24px var(--white);
  }
  .values {
    position: absolute; left: 105px; top: 390px;
    font-size: 40px; font-weight: 400; letter-spacing: .5px;
    text-shadow: 2px 2px 3px rgba(0,0,0,.35);
  }
  .quote-call {
    position: absolute; left: 125px; top: 537px;
    font-size: 22px; font-weight: 700; font-style: italic; letter-spacing: .4px;
  }
  .contact-line {
    position: absolute; left: 112px; top: 588px;
    font-size: 28px; font-weight: 400; letter-spacing: .3px;
  }
  .contact-line .contact-value { color: var(--accent-green); font-weight: 700; }
  .closing-line {
    position: absolute; left: 0; width: 1210px; top: 700px; text-align: center;
    font-size: 28px; font-weight: 400; letter-spacing: .8px;
    text-shadow: 2px 2px 3px rgba(0,0,0,.3);
  }
</style>
</head>
<body>
<main class="flyer">
  <div class="fence-visual" role="img" aria-label="Row of three green steel fence panels with lattice tops"></div>
  <div class="lattice-band lattice-band--upper" role="img" aria-label="Soft cream lattice pattern backdrop"></div>
  <div class="rule rule--upper"></div>
  <div class="rule rule--lower"></div>
  <div class="lattice-band lattice-band--lower" role="img" aria-label="Soft cream lattice pattern backdrop"></div>

  <h1 class="brand-name">Valley Copperpath Fencing</h1>
  <p class="service-line">Ferrowane Fencing Instalations</p>
  <p class="values">Reliabilty, Dependabilty and Genuine Quality</p>
  <p class="quote-call">Contact a Ferrowane Fence Specialist Today for a Free quote!</p>
  <p class="contact-line">Email: <span class="contact-value">copperpathfencing@quillmail.net</span> or Call: <span class="contact-value">0455 912 307</span></p>
  <p class="closing-line">Because it's not just a fence... It's your fence.</p>
</main>
</body>
</html>
```